Vitamin and Nutrition Ecommerce Site Needs a High End Website Design

We need a new and improved Homepage design for a leading Vitamin eCommerce business.
We supply our customers worldwide with leading brands of vitamin supplements and nutritional products at discounted prices.
The site design and layout must improve sales conversion and maximize the user experience staying on the site!

We will need to see;
A New Pillbox Lounge stylized font (no logo)
High-End Modern Design
Easy Sales Conversion Experience
Excellent Layout, Fast Navigation
Quality Font style, Stylish Colour Palette Selection
Appropriate Spacing
Call To Action to Improve Sales Conversion
Web page should Look Clean and Minimalist

The design should improve sales, communicate easy to find products, facilitate fast ordering, have a modern and professional appearance centered toward a predominately female consumer.

Thank you for your interest in this project!

Current design can be found on this link;
www.pillboxlounge.com.au/pillb/

Target Market(s)

80% Female 30-65 years

Industry/Entity Type

Business

Number of Pages Required

1 page

Colors

Designer to choose colors to be used in the design.

Requirements
Must have
• design must result improve sales conversion
• new Pillbox Lounge font design
• search field
• attractive clean modern design
• stylish font and colour palette selection
Nice to have
• white background
Should not have
• cluttered or busy layout
• confusing navigation

```html
<!DOCTYPE html>
<html lang="en">
<head>
<meta charset="utf-8">
<title>Pillbox Lounge – Home</title>
<link href="https://fonts.googleapis.com/css2?family=Open+Sans:wght@300;400;600;700&display=swap" rel="stylesheet">
<style>
  :root {
    --ink: #1c1c1c;
    --topbar: #222222;
    --teal: #0f9282;
    --teal-dark: #0b7566;
    --ring: #0d7462;
    --gold: #f3bf13;
    --logo: #f2b705;
    --muted: #6f6f6f;
    --mint: #effbfb;
    --white: #ffffff;
  }
  * { margin: 0; padding: 0; box-sizing: border-box; }
  html, body { width: 1200px; height: 1000px; overflow: hidden; }
  body { font-family: "Open Sans", Arial, sans-serif; color: var(--ink); background: var(--white); position: relative; }

  .topbar { height: 38px; background: var(--topbar); color: var(--white); font-size: 12px; font-weight: 600; display: flex; align-items: center; justify-content: space-between; padding: 0 23px; }
  .topbar .promo a { color: #19b8a2; text-decoration: none; }
  .topbar .account-links { display: flex; gap: 10px; }
  .topbar .account-links span.sep { opacity: .9; }

  .header { height: 74px; display: flex; align-items: center; padding: 0 24px; }
  .brand { font-size: 38px; font-weight: 400; color: var(--logo); letter-spacing: -0.5px; }
  .header-actions { margin-left: auto; display: flex; align-items: center; }
  .header-link { font-size: 14px; color: var(--ink); margin-right: 32px; text-decoration: none; }
  .auth { display: flex; height: 32px; border-radius: 16px; overflow: hidden; margin-left: 5px; }
  .auth a { color: var(--white); font-size: 13px; font-weight: 600; text-decoration: none; display: flex; align-items: center; }
  .auth .login { background: var(--teal); padding: 0 21px 0 22px; }
  .auth .register { background: var(--teal-dark); padding: 0 16px 0 12px; }
  .search { margin-left: 28px; width: 22px; height: 22px; }

  .main-nav { height: 38px; background: var(--teal); display: flex; align-items: center; justify-content: space-between; padding: 0 23px; }
  .main-nav a { color: var(--white); font-size: 12.5px; font-weight: 600; text-decoration: none; }

  .hero { height: 373px; position: relative;
    background: linear-gradient(90deg, #e6e9e8 0%, #f1f2f0 12%, #e7e3dd 22%, #f6f6f4 40%, #f2f3f2 55%, #dfe9d4 65%, #cfe3a8 75%, #dde8c9 85%, #f3f4f2 100%); }
  .slider-dots { position: absolute; left: 584px; top: 491px; display: flex; gap: 8px; }
  .slider-dots span { width: 11px; height: 11px; border-radius: 50%; background: #e4e9e7; }
  .slider-dots span.active { background: #b6dcc8; }

  .services { height: 477px; background: var(--mint); text-align: center; position: relative; }
  .services h2 { font-weight: 300; font-size: 40px; padding-top: 38px; letter-spacing: .3px; }
  .services .rule { width: 76px; height: 4px; background: var(--gold); margin: 13px auto 0; }
  .services .lead { font-size: 15px; margin-top: 23px; color: #333; }
  .connectors { position: absolute; left: 0; top: 200px; }
  .service { position: absolute; top: 205px; width: 260px; text-align: center; }
  .service h3 { margin-top: 26px; font-size: 19px; font-weight: 700; letter-spacing: .3px; }
  .service p { font-size: 17px; color: var(--muted); margin-top: 8px; line-height: 23px; }
  .service p .price { font-size: 20px; }
</style>
</head>
<body>
  <div class="topbar">
    <div class="promo">GET YOUR FREE PROMO CODE <a href="#">HERE</a></div>
    <div class="account-links">
      <span>MY ACCOUNT</span><span class="sep">I</span>
      <span>MY WISHLIST</span><span class="sep">I</span>
      <span>MY CART</span><span class="sep">I</span>
      <span>CHECKOUT</span>
    </div>
  </div>

  <header class="header">
    <div class="brand">Pillbox Lounge</div>
    <div class="header-actions">
      <a class="header-link" href="#">FAQS</a>
      <a class="header-link" href="#" style="margin-right:6px">ABOUT US</a>
      <div class="auth"><a class="login" href="#">LOGIN</a><a class="register" href="#">REGISTER</a></div>
      <svg class="search" viewBox="0 0 22 22" aria-label="Search"><circle cx="9" cy="9" r="6.5" fill="none" stroke="#9a9a9a" stroke-width="2.4"/><line x1="14" y1="14" x2="20" y2="20" stroke="#9a9a9a" stroke-width="3" stroke-linecap="round"/></svg>
    </div>
  </header>

  <nav class="main-nav">
    <a href="#">HOME</a><a href="#">BRANDS</a><a href="#">SUPPLEMENTS</a><a href="#">HAIRCARE</a>
    <a href="#">CHIROPRACTIC PILLOWS</a><a href="#">HEALTH CONDITIONS</a><a href="#">BEAUTY &amp; SKINCARE</a>
    <a href="#">GLUTEN FREE</a><a href="#">ONSALE</a>
  </nav>

  <section class="hero" role="img" aria-label="Woman drinking a glass of water in a bright kitchen beside a group of vitamin supplement bottles"></section>
  <div class="slider-dots"><span></span><span class="active"></span></div>

  <section class="services">
    <h2>Our Services</h2>
    <div class="rule"></div>
    <p class="lead">Here we mentioned some of our best services liked by our customers</p>

    <svg class="connectors" width="1200" height="200" viewBox="0 0 1200 200">
      <g stroke="var(--gold)" stroke-width="3.5" stroke-linecap="round" stroke-dasharray="0 6.5" fill="none">
        <line x1="252" y1="55" x2="362" y2="55"/>
        <line x1="258" y1="72" x2="260" y2="72"/>
        <line x1="535" y1="72" x2="662" y2="72"/>
        <line x1="812" y1="72" x2="940" y2="72"/>
      </g>
      <g fill="none" stroke="var(--ring)" stroke-width="3">
        <circle cx="184" cy="70" r="64"/>
        <circle cx="460" cy="70" r="64"/>
        <circle cx="737" cy="70" r="64"/>
        <circle cx="1013" cy="70" r="64"/>
      </g>
      <g fill="none" stroke="var(--ring)" stroke-width="4.5" stroke-linecap="round" stroke-linejoin="round">
        <polyline points="159,69 176,87 210,52"/>
        <polyline points="435,69 452,87 486,52"/>
        <polyline points="712,69 729,87 763,52"/>
        <polyline points="988,69 1005,87 1039,52"/>
      </g>
    </svg>

    <div class="service" style="left:50px; top:343px"><h3>FREE SHIPPING</h3><p>For all orders above<br><span class="price">$99 !</span></p></div>
    <div class="service" style="left:326px; top:343px"><h3>OFFICIAL STOCKLIST</h3><p>Of more the 100<br>products.</p></div>
    <div class="service" style="left:603px; top:343px"><h3>2 FREE SAMPLES</h3><p>On all orders above<br><span class="price">$99 !</span></p></div>
    <div class="service" style="left:869px; top:343px; width:290px"><h3>SHOPSURE TRUSTED STORE</h3><p>For all orders above<br><span class="price">$99 !</span></p></div>
  </section>
</body>
</html>
```